Website Design for Law Firm

We need a fresh new website design for our client 'Torvek Legal' who specialises as a Criminal, Traffic & Civil Lawyer in Perth, Western Australia. We are looking for a very clean, professional and elegant look for the website, a presence of power and class needed as he deals with high end clients. Black, Silver and hints of gold need to run through the design without making the site look too dark. We are after a very modern, spacious web look, use of large readable text with links to social media (such as Facebook, Google+, Twitter, LinkedIn) to stand out and his contact details to be made very predominate.

Reason: Public holidays here in Australia, need more business hours to discuss designs with client.

Reason: Client needs more time to look through designs.

Reason: Client is going over last of designs. Design will be picked early next week!

Law Firm

```html
<!DOCTYPE html>
<html lang="en">
<head>
<meta charset="utf-8">
<title>Torvek Legal</title>
<link rel="stylesheet" href="https://fonts.googleapis.com/css2?family=Cinzel:wght@400;700&family=Great+Vibes&family=Jost:wght@400;500;600&family=Noto+Sans:wght@400;700&display=swap">
<style>
:root{
  --black:#151618;
  --ink:#1d1d1f;
  --gold:#c9a24a;
  --gold-dark:#8a6a24;
  --silver-top:#f7f8f9;
  --silver-bottom:#cfd2d8;
  --page:#eef0ef;
  --card-top:#d7dde0;
  --card-bottom:#eef1f1;
  --white:#ffffff;
  --footer-text:#e8e8e8;
}
*{margin:0;padding:0;box-sizing:border-box}
html,body{width:1200px;height:1000px;overflow:hidden}
body{background:var(--page);font-family:"Noto Sans",sans-serif;color:var(--ink);position:relative}

.site-header{position:absolute;left:0;top:0;width:1200px;height:128px;
  background:linear-gradient(var(--silver-top) 0%,#eceef1 55%,var(--silver-bottom) 100%)}
.brand{position:absolute;left:0;width:1200px;top:20px;display:flex;justify-content:center;align-items:center;gap:8px}
.brand-mark{width:14px;height:14px;background:var(--gold)}
.brand-name{font-family:"Jost",sans-serif;font-weight:600;font-size:22px;color:var(--black);letter-spacing:1px}

.main-nav{position:absolute;left:306px;top:77px;height:28px;display:flex;
  background:var(--black);border-left:3px solid var(--gold);border-right:3px solid var(--gold)}
.main-nav a{display:block;height:28px;line-height:27px;padding:0 12px;color:var(--white);text-decoration:none;
  font-family:"Jost",sans-serif;font-size:13px;border-right:2px solid var(--gold-dark);position:relative}
.main-nav a:last-child{border-right:none}
.main-nav a.has-sub::after{content:"";position:absolute;left:50%;bottom:2px;margin-left:-3px;
  border-left:3px solid transparent;border-right:3px solid transparent;border-top:3px solid var(--white)}

.hero{position:absolute;left:0;top:128px;width:1200px;height:305px;
  background:radial-gradient(ellipse at 45% 50%,#6b4a33 0%,#3e2a1d 45%,#241a14 100%)}
.hero-photo{position:absolute;inset:0;
  background:linear-gradient(90deg,rgba(90,120,80,.55) 0%,rgba(120,150,110,.35) 30%,rgba(0,0,0,0) 55%,rgba(30,20,14,.4) 100%)}
.hero-title{position:absolute;right:235px;top:60px;text-align:right;color:var(--white)}
.hero-title h1{font-family:"Cinzel",serif;font-weight:400;font-size:26px;letter-spacing:1px;line-height:30px}
.hero-title p{font-family:"Jost",sans-serif;font-weight:600;font-size:11px;line-height:13px;text-transform:uppercase;letter-spacing:.3px}

.hero-rule{position:absolute;left:0;top:433px;width:1200px;height:20px;background:var(--white)}
.hero-rule::after{content:"";position:absolute;left:0;bottom:-3px;width:1200px;height:3px;background:var(--black)}

.welcome{position:absolute;left:234px;top:464px;width:600px}
.welcome h2{font-family:"Great Vibes",cursive;font-weight:400;font-size:42px;line-height:52px;color:var(--ink)}
.welcome p{margin-top:14px;font-size:12px;line-height:14px;letter-spacing:.2px}

.features{position:absolute;left:234px;top:627px;display:flex;gap:19px}
.feature{width:231px;text-align:center}
.feature-body{height:118px;background:linear-gradient(var(--card-top) 0%,var(--card-bottom) 35%,var(--page) 100%);padding:4px 4px 0}
.feature h3{font-family:"Jost",sans-serif;font-weight:600;font-size:13px;line-height:12px;height:28px;display:flex;align-items:center;justify-content:center;margin-bottom:3px}
.feature p{font-size:9px;line-height:11.3px}
.read-more{display:inline-block;margin-top:8px;width:106px;height:17px;line-height:16px;background:var(--black);
  border:1px solid var(--gold-dark);color:var(--white);font-family:"Cinzel",serif;font-size:10px;text-decoration:none}

.site-footer{position:absolute;left:0;top:801px;width:1200px;height:199px;background:var(--black);border-top:2px solid var(--gold)}
.footer-nav{position:absolute;left:0;top:6px;width:1200px;text-align:center;font-family:"Jost",sans-serif;font-size:10px;color:var(--white)}
.footer-nav a{color:var(--white);text-decoration:none}
.footer-nav span{margin:0 7px}
.footer-links{position:absolute;top:32px;list-style:none;font-size:7px;font-weight:700;color:var(--footer-text)}
.footer-links li{height:14.2px;line-height:10px;padding-left:8px;position:relative}
.footer-links li::before{content:"";position:absolute;left:0;top:3px;width:3px;height:3px;border-radius:50%;background:var(--gold)}
.copyright{position:absolute;left:0;top:179px;width:1200px;text-align:center;font-size:6px;color:var(--footer-text)}
</style>
</head>
<body>
<header class="site-header">
  <div class="brand"><span class="brand-mark"></span><span class="brand-name">TORVEK LEGAL</span></div>
  <nav class="main-nav">
    <a href="#">Home</a>
    <a href="#" class="has-sub">Legal Topics</a>
    <a href="#">Post Your Case</a>
    <a href="#" class="has-sub">Find a Lawyer</a>
    <a href="#" class="has-sub">Legal Articles</a>
    <a href="#">Contacts</a>
  </nav>
</header>

<section class="hero">
  <div class="hero-photo" role="img" aria-label="Photo of a law office with leather chairs, a polished desk and large windows"></div>
  <div class="hero-title">
    <h1>Lorem Ipsum it Samet</h1>
    <p>Duis sed odio sit amet nibh vulputate<br>cursus a sit amet mauris.</p>
  </div>
</section>
<div class="hero-rule"></div>

<section class="welcome">
  <h2>Welcome</h2>
  <p>Offering a wide variety of different fields and disciplines<br>
  Lorem ipsum dolor sit amet, consectetuer adipiscing elit. Praesent vestibulum molestie lacus.
  Aenean nonummy hendrerit mauris. Phasellus porta. Fusce suscipit varius mi. Lorem ipsum dolor
  sit amet, consectetuer adipiscing elit. Praesent vestibulum molestie lacus.</p>
</section>

<section class="features">
  <article class="feature">
    <div class="feature-body">
      <h3>Improve your skills with our help!</h3>
      <p>Lorem ipsum dolor sit amet, consectetuer adipiscing elit. Praesent vestibulum molestie lacus. Aenean nonummy hendrerit mauris. Phasellus porta. Fusce suscipit varius mi. Lorem ipsum dolor sit amet, consectetuer adipiscing elit. Praesent vestibulum molestie lacus. Morbi nunc odio, gravida at.</p>
    </div>
    <a href="#" class="read-more">Read More</a>
  </article>
  <article class="feature">
    <div class="feature-body">
      <h3>Developing a life-long<br>love of learning!</h3>
      <p>Lorem ipsum dolor sit amet, consectetuer adipiscing elit. Praesent vestibulum molestie lacus. Aenean non hendrerit mauris. Phasellus porta. Fusce suscipit varius mi. Lorem ipsum dolor sit amet, consectetuer adipiscing elit. Praesent vestibulum molestie lacus.</p>
    </div>
    <a href="#" class="read-more">Read More</a>
  </article>
  <article class="feature">
    <div class="feature-body">
      <h3>Intensify your professional image!</h3>
      <p>Lorem ipsum dolor sit amet, consectetuer adipiscing elit. Praesent vestibulum molestie lacus. Aenean nonummy hendrerit mauris. Phasellus porta. Fusce suscipit varius mi. Lorem ipsum dolor sit amet, consectetuer adipiscing elit. Praesent vestibulum molestie lacus. Morbi nunc odio, gravida at.</p>
    </div>
    <a href="#" class="read-more">Read More</a>
  </article>
</section>

<footer class="site-footer">
  <nav class="footer-nav">
    <a href="#">Home</a><span>|</span><a href="#">Legal Topics</a><span>|</span><a href="#">Post Your Case</a><span>|</span><a href="#">Find a Lawyer</a><span>|</span><a href="#">Legal Articles</a><span>|</span><a href="#">Contacts</a>
  </nav>
  <ul class="footer-links" style="left:234px">
    <li>Lorem Ipsum.</li><li>Proin gravida auctor aliquet.</li><li>Aenean sollicitudin elit.</li><li>.Duis sed odio sit amet nibh</li><li>vulputate cursus a sit amet</li><li>mauris. Morbi accumsan ipsum</li><li>velit. Nam nec tellus a odio</li><li>tincidunt auctor a ornare odio.</li><li>Sed non &nbsp;mauris vitae erat</li>
  </ul>
  <ul class="footer-links" style="left:421px">
    <li>Lorem Ipsum.</li><li>Proin gravida auctor aliquet.</li><li>Aenean sollicitudin elit.</li><li>.Duis sed odio sit amet nibh</li><li>vulputate cursus a sit amet</li><li>mauris. Morbi accumsan ipsum</li><li>velit. Nam nec tellus a odio</li><li>tincidunt auctor a ornare odio.</li><li>Sed non &nbsp;mauris vitae erat</li>
  </ul>
  <ul class="footer-links" style="left:609px">
    <li>Lorem Ipsum.</li><li>Proin gravida auctor aliquet.</li><li>Aenean sollicitudin elit.</li><li>.Duis sed odio sit amet nibh</li><li>vulputate cursus a sit amet</li><li>mauris. Morbi accumsan ipsum</li><li>velit. Nam nec tellus a odio</li><li>tincidunt auctor a ornare odio.</li><li>Sed non &nbsp;mauris vitae erat</li>
  </ul>
  <ul class="footer-links" style="left:797px">
    <li>Lorem Ipsum.</li><li>Proin gravida auctor aliquet.</li><li>Aenean sollicitudin elit.</li><li>.Duis sed odio sit amet nibh</li><li>vulputate cursus a sit amet</li><li>mauris. Morbi accumsan ipsum</li><li>velit. Nam nec tellus a odio</li><li>tincidunt auctor a ornare odio.</li><li>Sed non &nbsp;mauris vitae erat</li>
  </ul>
  <p class="copyright">Copyright © 2014 Torvek Legal</p>
</footer>
</body>
</html>
```